Corporate Brochure Cover Design

We need a design for a corporate A4 Size portfolio cover (front and back) which we will be distributing. to our commercial clients.

We are a professional plumbing company that is an industry leader for service we provide to our clients and technology we use. The design needs to incorporate the colours black, red, white and silver and needs to include our logo. We dont have any slogans or mottos... If you wanted to use something it could be "Delivering exceptional service...Always!" however i dont want it to b the focal point of the cover.

Im looking for something professional and modern that has the WOW factor!

Size is A4 - both front and back covers. You can include pictures as well or sample pictures of where we can source and put our own team pictures.

if you have any questions, please do not hesitate to contact me.

Target Market(s)

Our commercial & strata clients - professional industry.

Industry/Entity Type

Commercial

Font styles to use
Sans Serif

Requirements
Must have
• Red, black, white, silver as the colour scheme.
• Include the logo.
Nice to have
• Modern design and something that makes the client go WOW before they open the brochure.
Should not have
• lots of text

```html
<!DOCTYPE html>
<html lang="en">
<head>
<meta charset="utf-8">
<title>Conduit Portfolio Cover – Front and Back</title>
<link href="https://fonts.googleapis.com/css2?family=Oswald:wght@400;600&family=Open+Sans:wght@400;600&display=swap" rel="stylesheet">
<style>
  :root {
    --black: #1c1b1c;
    --red: #d0192b;
    --white: #ffffff;
    --silver: #c9cbce;
    --stage: #e4e5e7;
    --photo-blue: #5b7fb0;
    --photo-light: #e6e9ee;
  }
  * { margin: 0; padding: 0; box-sizing: border-box; }
  html, body { width: 1200px; height: 800px; overflow: hidden; }
  body { background: var(--stage); font-family: "Open Sans", sans-serif; }

  .cover-spread {
    position: absolute; left: 91px; top: 40px;
    width: 1018px; height: 720px;
    box-shadow: 0 6px 24px rgba(0,0,0,.25);
  }
  .cover-art { position: absolute; inset: 0; width: 1018px; height: 720px; display: block; }

  .wordmark {
    font-family: "Oswald", sans-serif; font-weight: 600;
    color: var(--white); letter-spacing: 2px; line-height: 1;
    display: flex; align-items: center; gap: 10px;
  }
  .wordmark-dot { border-radius: 50%; background: var(--red); flex: none; }
  .service-line {
    font-family: "Open Sans", sans-serif; font-weight: 600;
    color: var(--silver); text-transform: uppercase; letter-spacing: 1px;
    white-space: nowrap;
  }

  /* front cover */
  .front-brand { position: absolute; left: 620px; top: 92px; width: 330px; text-align: left; }
  .front-brand .wordmark { font-size: 62px; }
  .front-brand .wordmark-dot { width: 22px; height: 22px; }
  .front-brand .service-line { font-size: 10px; margin-top: 8px; }
  .front-brand .service-sub { font-size: 7px; color: var(--silver); letter-spacing: 1px; margin-top: 3px; font-weight: 600; }

  .slogan {
    position: absolute; left: 600px; top: 250px; width: 360px;
    font-family: "Oswald", sans-serif; font-weight: 400;
    color: var(--white); font-size: 23px; letter-spacing: 1px; text-transform: uppercase; line-height: 1.35;
  }
  .slogan span { display: block; }
  .slogan .slogan-second { text-align: right; }

  /* back cover */
  .back-brand { position: absolute; left: 0; top: 300px; width: 509px; display: flex; flex-direction: column; align-items: center; }
  .back-brand .wordmark { font-size: 30px; }
  .back-brand .wordmark-dot { width: 11px; height: 11px; }
  .back-brand .service-line { font-size: 5px; margin-top: 4px; }

  .contact-list { position: absolute; left: 0; top: 410px; width: 509px; list-style: none; text-align: center; }
  .contact-item { color: var(--white); font-size: 10px; margin-bottom: 12px; display: flex; flex-direction: column; align-items: center; gap: 5px; }
  .contact-icon { width: 18px; height: 18px; display: block; }
</style>
</head>
<body>
  <main class="cover-spread">
    <svg class="cover-art" viewBox="0 0 1018 720" xmlns="http://www.w3.org/2000/svg">
      <defs>
        <linearGradient id="desk-photo" x1="0" y1="0" x2="0" y2="1">
          <stop offset="0" stop-color="var(--photo-light)"/>
          <stop offset="0.55" stop-color="#dfe2e7"/>
          <stop offset="0.56" stop-color="var(--photo-blue)"/>
          <stop offset="1" stop-color="#3f6aa6"/>
        </linearGradient>
        <linearGradient id="plumber-photo" x1="0" y1="0" x2="1" y2="1">
          <stop offset="0" stop-color="#eceef1"/>
          <stop offset="0.5" stop-color="#c8ced6"/>
          <stop offset="1" stop-color="#4c6e9e"/>
        </linearGradient>
      </defs>

      <!-- back cover -->
      <rect class="back-panel" x="0" y="0" width="509" height="720" fill="var(--black)"/>
      <path class="back-photo-band" d="M44,0 H509 V120 C440,280 190,305 90,170 C58,125 46,60 44,0 Z" fill="var(--red)"/>
      <path class="back-photo-edge" d="M54,0 H509 V112 C438,262 196,285 100,160 C70,118 57,58 54,0 Z" fill="var(--white)"/>
      <path class="back-photo" role="img" aria-label="Photo of hands on a laptop above plumbing tools laid on a blue desk"
            d="M60,0 H509 V104 C436,250 200,272 108,152 C80,114 63,56 60,0 Z" fill="url(#desk-photo)"/>

      <!-- front cover -->
      <rect class="front-panel" x="509" y="0" width="509" height="720" fill="var(--black)"/>
      <path class="front-photo-band" d="M540,720 C600,540 770,428 1018,426 V720 Z" fill="var(--red)"/>
      <path class="front-photo-edge" d="M566,720 C624,560 780,456 1018,454 V720 Z" fill="var(--silver)"/>
      <path class="front-photo" role="img" aria-label="Photo of a smiling plumber in a blue cap and work shirt beside under-sink pipework"
            d="M578,720 C636,568 786,466 1000,464 V720 Z" fill="url(#plumber-photo)"/>

      <line class="fold" x1="509" y1="0" x2="509" y2="720" stroke="#000" stroke-opacity=".35" stroke-width="1"/>
    </svg>

    <!-- front cover text -->
    <div class="front-brand">
      <div class="wordmark"><span class="wordmark-dot"></span>CONDUIT</div>
      <div class="service-line">Plumbing and property service professionals</div>
      <div class="service-sub">24/7 EMERGENCY RESPONSE</div>
    </div>
    <p class="slogan">
      <span class="slogan-first">Delivering exceptional</span>
      <span class="slogan-second">service...always!</span>
    </p>

    <!-- back cover text -->
    <div class="back-brand">
      <div class="wordmark"><span class="wordmark-dot"></span>CONDUIT</div>
      <div class="service-line">Plumbing and property service professionals</div>
    </div>
    <ul class="contact-list">
      <li class="contact-item">
        <svg class="contact-icon" viewBox="0 0 20 20"><circle cx="10" cy="10" r="10" fill="var(--white)"/><path d="M7 5 L9 7 L8 8.5 C8.6 10 10 11.4 11.5 12 L13 11 L15 13 L13.5 15 C9.5 14.8 5.2 10.5 5 6.5 Z" fill="var(--black)"/></svg>
        <span>555.014.2870</span>
      </li>
      <li class="contact-item">
        <svg class="contact-icon" viewBox="0 0 20 20"><circle cx="10" cy="10" r="10" fill="var(--white)"/><rect x="5" y="6.5" width="10" height="7" fill="var(--black)"/><path d="M5 6.5 L10 10.5 L15 6.5" fill="none" stroke="var(--white)" stroke-width="1"/></svg>
        <span>Email address</span>
      </li>
      <li class="contact-item">
        <svg class="contact-icon" viewBox="0 0 20 20"><circle cx="10" cy="10" r="10" fill="var(--white)"/><circle cx="10" cy="10" r="5.5" fill="none" stroke="var(--black)" stroke-width="1.2"/><ellipse cx="10" cy="10" rx="2.3" ry="5.5" fill="none" stroke="var(--black)" stroke-width="1"/><line x1="4.5" y1="10" x2="15.5" y2="10" stroke="var(--black)" stroke-width="1"/></svg>
        <span>www.conduitservices.com</span>
      </li>
    </ul>
  </main>
</body>
</html>
```